電子書籍の表紙デザインをお願い致します。

一冊目の『静かな朝の見送り方』に引き続き、今回は『月影ノート』の本になります。

たくさんの悲しみを乗り越えた私の経験をペットちゃんを亡くされ、悲しんでいらっしゃる飼い主様に読んで頂きたいと思います。

出来ましたら、本の中の私の言葉をお入れ頂けたら嬉しいです。

前回のデザイン募集の時はたくさんの素敵なデザインの応募がありとても悩みました。
今回もとても楽しみにしておりますので宜しくお願い致します。

文字だけの表紙でなく、夜空の星、虹、あるいは飼い主様とペットちゃんなどの絵、写真、シルエット等を入れてお願いしたいです。

こちらを選んだ理由は
お空に浮かんだシルエットが亡き愛犬に似ていたことと、
希望であった本文からの言葉も気に入りました。

そして、前回の『森の小径を歩いた君へ、やさしい日々をいつまでも』
『静かな朝の見送り方』の表紙と同じく『森の小径を歩いた君へ』と入れてくれたことです。

今回もたくさんの方からご提案頂き、ありがとうございました。
どの作品も非常に良く出来ていて悩みました。
次回、また『小さな旅支度、明日の旅支度』の出版を考えておりますので宜しくお願い致します。

```html
<!DOCTYPE html>
<html lang="ja">
<head>
<meta charset="utf-8">
<title>月影ノート 表紙</title>
<link rel="stylesheet" href="https://fonts.googleapis.com/css2?family=Shippori+Mincho:wght@400;500;600&display=swap">
<style>
  :root {
    --ink-teal: #1e4956;
    --ink-soft: #35565f;
    --gauze-light: #f5f4f1;
    --gauze-mid: #dedbd5;
    --gauze-shadow: #b9b5ae;
    --gauze-deep: #9d9891;
    --fur-warm: #e9dcc4;
    --fur-deep: #d6c6a8;
    --accent-yellow: #f0d54e;
    --edge-pink: #e9c9cc;
  }
  * { margin: 0; padding: 0; box-sizing: border-box; }
  html, body { width: 847px; height: 1200px; overflow: hidden; background: #fff; }
  .cover {
    position: relative;
    width: 847px;
    height: 1200px;
    overflow: hidden;
    font-family: "Shippori Mincho", serif;
    color: var(--ink-teal);
  }
  .cover-photo {
    position: absolute;
    inset: 0;
    background:
      radial-gradient(ellipse 9% 6% at 53% 12%, var(--accent-yellow) 0%, rgba(240,213,78,0.6) 55%, rgba(240,213,78,0) 100%),
      radial-gradient(ellipse 40% 22% at 28% 30%, var(--fur-warm) 0%, var(--fur-deep) 45%, rgba(214,198,168,0) 100%),
      radial-gradient(ellipse 22% 12% at 18% 45%, rgba(120,110,98,0.55) 0%, rgba(120,110,98,0) 100%),
      radial-gradient(ellipse 50% 30% at 70% 72%, var(--gauze-light) 0%, rgba(245,244,241,0) 100%),
      radial-gradient(ellipse 40% 35% at 10% 85%, var(--gauze-deep) 0%, rgba(157,152,145,0) 100%),
      radial-gradient(ellipse 30% 20% at 95% 95%, var(--gauze-shadow) 0%, rgba(185,181,174,0) 100%),
      linear-gradient(180deg, rgba(233,201,204,0) 0%, rgba(233,201,204,0) 100%),
      linear-gradient(155deg, var(--gauze-mid) 0%, var(--gauze-light) 35%, var(--gauze-mid) 60%, var(--gauze-shadow) 100%);
  }
  .cover-edge {
    position: absolute;
    top: 0; right: 0;
    width: 34px; height: 300px;
    background: linear-gradient(180deg, var(--edge-pink) 0%, rgba(233,201,204,0) 100%);
  }
  .vertical { position: absolute; writing-mode: vertical-rl; }
  .subtitle {
    top: 60px; left: 752px;
    font-size: 21px; font-weight: 500;
    letter-spacing: 2px;
    color: var(--ink-soft);
  }
  .title {
    top: 85px; left: 648px;
    font-size: 100px; font-weight: 600;
    letter-spacing: 24px;
    line-height: 1;
  }
  .title-rule {
    position: absolute;
    top: 470px; left: 778px;
    width: 3px; height: 120px;
    background: var(--ink-teal);
  }
  .message {
    top: 395px; left: 512px;
    font-size: 38px; font-weight: 500;
    line-height: 1.55;
    letter-spacing: 4px;
  }
  .colophon {
    top: 815px; left: 30px;
    font-size: 14px;
    line-height: 1.8;
    letter-spacing: 0.5px;
    color: var(--ink-soft);
    white-space: nowrap;
  }
</style>
</head>
<body>
  <main class="cover">
    <div class="cover-photo" role="img" aria-label="ガーゼに包まれて安らかに眠る白い犬の写真"></div>
    <div class="cover-edge" aria-hidden="true"></div>
    <p class="vertical subtitle">〜否定・交渉（願い）・怒り・受容〜</p>
    <h1 class="vertical title">月影ノート</h1>
    <span class="title-rule" aria-hidden="true"></span>
    <p class="vertical message">あなたは悲しみと<br>どう向き合いますか</p>
    <p class="vertical colophon">表紙写真　森の小径を歩いた君へ（ゆき）<br>二〇二一年八月　月野しずく　著</p>
  </main>
</body>
</html>
```